Card Design for my dog training business Rustpaw Obedience

Need a business card design for my dog training business with my new logo. Want the card to come off professional yet fun. Want it to be very eye catchy as well. I normally have these at vet clinics, pet stores, and groomers. so need it to look better than my competitors.
Target Market(s)
dog owners
Industry/Entity Type
Dog Training
Contact Information for Business Card
needs logo, my name and info
Font styles to use
Serif
Colors
0255a3
ffffff
ec1f27
000000
333333
fbfbfb
Requirements
Must have
- Rustpaw Obedience
- Hollis Brandt
- 415 903 2267
- info@rustpawobedience.example
- www.rustpawobedience.example

```html
<!DOCTYPE html>
<html lang="en">
<head>
<meta charset="utf-8">
<title>Rustpaw Obedience – Business Card</title>
<link href="https://fonts.googleapis.com/css2?family=Libre+Baskerville:ital,wght@0,400;1,400&display=swap" rel="stylesheet">
<style>
  :root {
    --ink: #000000;
    --paper: #ffffff;
    --stage: #e9e6e6;
    --soft: #fbfbfb;
    --serif: "Libre Baskerville", Georgia, serif;
  }
  * { margin: 0; padding: 0; box-sizing: border-box; }
  html, body { width: 1200px; height: 862px; overflow: hidden; background: var(--stage); }
  .stage { position: relative; width: 1200px; height: 862px; }
  .card {
    position: absolute; top: 151px; width: 320px; height: 560px;
    overflow: hidden; box-shadow: 0 10px 30px rgba(0,0,0,.18);
    font-family: var(--serif);
  }
  .card--front { left: 220px; }
  .card--back { left: 660px; }
  .card__bg { position: absolute; inset: 0; width: 100%; height: 100%; }
  .brand {
    position: absolute; left: 0; right: 0; text-align: center;
    display: flex; flex-direction: column; align-items: center; gap: 14px;
  }
  .brand__dot { width: 18px; height: 18px; border-radius: 50%; background: var(--ink); }
  .brand__name {
    font-size: 26px; line-height: 1.25; color: var(--ink); font-weight: 400;
    letter-spacing: .02em;
  }
  .card--front .brand { top: 240px; }
  .card--back .brand { top: 92px; }
  .tagline {
    position: absolute; top: 412px; left: 20px; right: 20px; text-align: center;
    font-style: italic; font-size: 10.5px; color: var(--ink);
  }
  .holder {
    position: absolute; top: 376px; left: 0; right: 0; text-align: center;
    color: var(--paper); font-size: 20px; font-weight: 400; letter-spacing: .03em;
  }
  .divider {
    position: absolute; top: 418px; left: 34px; right: 34px; height: 26px;
    display: flex; align-items: center; gap: 8px;
  }
  .divider__rule { flex: 1; height: 1px; background: var(--paper); }
  .divider__icon {
    width: 24px; height: 24px; border-radius: 50%; background: var(--paper);
    display: flex; align-items: center; justify-content: center;
  }
  .contact {
    position: absolute; top: 462px; left: 0; right: 0; text-align: center;
    list-style: none; color: var(--paper); font-size: 13px; line-height: 1.6;
  }
</style>
</head>
<body>
<main class="stage">
  <section class="card card--front" aria-label="Card front">
    <svg class="card__bg" viewBox="0 0 320 560" aria-hidden="true">
      <rect width="320" height="560" fill="#000"/>
      <polygon points="0,190 160,100 320,190 320,560 0,560" fill="#fff"/>
    </svg>
    <div class="brand">
      <span class="brand__dot"></span>
      <span class="brand__name">Rustpaw<br>Obedience</span>
    </div>
    <p class="tagline">“Calm dogs and happy homes, one lesson at a time.”</p>
  </section>

  <section class="card card--back" aria-label="Card back">
    <svg class="card__bg" viewBox="0 0 320 560" aria-hidden="true">
      <rect width="320" height="560" fill="#000"/>
      <polygon points="0,0 320,0 320,250 160,335 0,250" fill="#fff"/>
    </svg>
    <div class="brand">
      <span class="brand__dot"></span>
      <span class="brand__name">Rustpaw<br>Obedience</span>
    </div>
    <h1 class="holder">HOLLIS BRANDT</h1>
    <div class="divider">
      <span class="divider__rule"></span>
      <span class="divider__icon">
        <svg width="12" height="12" viewBox="0 0 24 24" aria-label="Phone"><path fill="#000" d="M6.6 10.8a15.1 15.1 0 0 0 6.6 6.6l2.2-2.2a1 1 0 0 1 1-.25 11.4 11.4 0 0 0 3.6.57 1 1 0 0 1 1 1V20a1 1 0 0 1-1 1A17 17 0 0 1 3 4a1 1 0 0 1 1-1h3.5a1 1 0 0 1 1 1c0 1.25.2 2.45.57 3.57a1 1 0 0 1-.25 1z"/></svg>
      </span>
      <span class="divider__icon">
        <svg width="12" height="12" viewBox="0 0 24 24" aria-label="Email"><rect x="2" y="5" width="20" height="14" fill="#000"/><path d="M2 5l10 8 10-8" fill="none" stroke="#fff" stroke-width="2"/></svg>
      </span>
      <span class="divider__icon">
        <svg width="13" height="13" viewBox="0 0 24 24" aria-label="Website"><g fill="none" stroke="#000" stroke-width="2"><circle cx="12" cy="12" r="9"/><ellipse cx="12" cy="12" rx="4" ry="9"/><path d="M3 12h18"/></g></svg>
      </span>
      <span class="divider__rule"></span>
    </div>
    <ul class="contact">
      <li>415 903 2267</li>
      <li>info@rustpawobedience.example</li>
      <li>www.rustpawobedience.example</li>
    </ul>
  </section>
</main>
</body>
</html>
```